Brightmoor Partners Branding Revamp

We are a consulting company, looking for a way to display and promote our brand. We have 2 sides to the business- Brightmoor (financial) and Partners (cyber security). The financial side products relate to business necessities: card processing, website design/hosting/maintenance, VoIP phone systems. The cyber security side promotes a bundled package of 4 solutions: network vulnerability scan, dark web scan, anti-ransomeware/malware software, and image-level backups. We want people to understand that partnering with Brightmoor Partners gives them “Elevated Peace of Mind” (tagline). Current badge and logos uploaded.

Target Market(s)

Small businesses

Contact Information for Business Card

Lena Marwick, Vice President, lena@brightmoorpartners.example, 555-806-1937, www.brightmoorpartners.example

Requirements
Nice to have
• I do prefer the darker background for front and back

```html
<!DOCTYPE html>
<html lang="en">
<head>
<meta charset="utf-8">
<title>Brightmoor Partners — Business Card</title>
<link rel="stylesheet" href="https://fonts.googleapis.com/css2?family=Montserrat:wght@400;500;700;800&display=swap">
<style>
  :root {
    --page: #ffffff;
    --card: #05080a;
    --red: #e8202a;
    --white: #ffffff;
    --rule: #f3ecea;
  }
  * { box-sizing: border-box; margin: 0; padding: 0; }
  html, body { width: 1200px; height: 1000px; overflow: hidden; background: var(--page); }
  body { position: relative; font-family: "Montserrat", sans-serif; }

  .card {
    position: absolute;
    left: 294px;
    width: 612px;
    height: 349px;
    background: var(--card);
    overflow: hidden;
  }
  .card--front { top: 143px; }
  .card--back { top: 508px; }

  /* brand lockup: plain circle + name */
  .brand { position: absolute; text-align: center; color: var(--white); }
  .brand__dot { display: block; margin: 0 auto; border-radius: 50%; background: var(--red); }
  .brand__name { font-weight: 700; white-space: nowrap; }

  .card--front .brand { left: 38px; top: 128px; width: 200px; }
  .card--front .brand__dot { width: 40px; height: 40px; }
  .card--front .brand__name { margin-top: 14px; font-size: 14px; letter-spacing: 2.5px; }

  .card--back .brand { left: 0; top: 82px; width: 612px; }
  .card--back .brand__dot { width: 110px; height: 110px; }
  .card--back .brand__name { margin-top: 36px; font-size: 27px; letter-spacing: 6px; }

  /* person */
  .person { position: absolute; right: 43px; top: 60px; text-align: right; }
  .person__name { color: var(--red); font-weight: 800; font-size: 29px; line-height: 1; letter-spacing: -0.3px; }
  .person__title { color: var(--white); font-weight: 700; font-size: 14px; letter-spacing: 1.6px; margin-top: 6px; }

  .rule { position: absolute; right: 43px; width: 206px; height: 2px; background: linear-gradient(90deg, var(--rule) 0 80%, var(--red) 80% 100%); }
  .rule--heavy { top: 122px; height: 5px; }
  .rule--one { top: 209px; }
  .rule--two { top: 261px; }

  /* contacts */
  .contact { position: absolute; right: 43px; display: flex; align-items: center; gap: 12px; color: var(--white); font-size: 17px; font-weight: 500; white-space: nowrap; }
  .contact--phone { top: 168px; }
  .contact--web { top: 218px; }
  .contact--mail { top: 270px; }
  .contact__icon { width: 34px; height: 34px; border-radius: 50%; background: var(--red); display: flex; align-items: center; justify-content: center; }
  .contact__icon svg { width: 20px; height: 20px; }
</style>
</head>
<body>

<section class="card card--front">
  <div class="brand">
    <span class="brand__dot"></span>
    <p class="brand__name">BRIGHTMOOR PARTNERS</p>
  </div>

  <div class="person">
    <h1 class="person__name">LENA MARWICK</h1>
    <p class="person__title">VICE PRESIDENT</p>
  </div>

  <div class="rule rule--heavy"></div>

  <div class="contact contact--phone">
    <span>555-806-1937</span>
    <span class="contact__icon">
      <svg viewBox="0 0 24 24"><path fill="#fff" d="M6.6 10.8a15 15 0 0 0 6.6 6.6l2.2-2.2a1 1 0 0 1 1-.25 11.4 11.4 0 0 0 3.6.57 1 1 0 0 1 1 1V20a1 1 0 0 1-1 1A17 17 0 0 1 3 4a1 1 0 0 1 1-1h3.5a1 1 0 0 1 1 1c0 1.25.2 2.45.57 3.57a1 1 0 0 1-.25 1z"/></svg>
    </span>
  </div>
  <div class="rule rule--one"></div>

  <div class="contact contact--web">
    <span>www.brightmoorpartners.example</span>
    <span class="contact__icon">
      <svg viewBox="0 0 24 24" fill="none" stroke="#fff" stroke-width="1.4"><circle cx="12" cy="12" r="9"/><ellipse cx="12" cy="12" rx="4" ry="9"/><path d="M3 12h18M4.5 7.5h15M4.5 16.5h15M12 3v18"/></svg>
    </span>
  </div>
  <div class="rule rule--two"></div>

  <div class="contact contact--mail">
    <span>lena@brightmoorpartners.example</span>
    <span class="contact__icon">
      <svg viewBox="0 0 24 24" fill="none" stroke="#fff" stroke-width="1.5"><rect x="3" y="6" width="18" height="12" rx="1"/><path d="M3 6l9 7 9-7M3 18l7-6M21 18l-7-6"/></svg>
    </span>
  </div>
</section>

<section class="card card--back">
  <div class="brand">
    <span class="brand__dot"></span>
    <p class="brand__name">BRIGHTMOOR PARTNERS</p>
  </div>
</section>

</body>
</html>
```